RM Tomás Ferrier (Business Card)

Hi designers, in this work, I'm looking for an sophisticated stylish, elegant and proffesional personal card. We have a laboratory of pathology automated, with equipments high quality.
In this web the designers, have created my business logo, the name is "RM Tomás Ferrier"
In our lab, we principal work is to prepare the biopsies for further diagnostic of diseases like cancer, tumors, etc.
I need that the first face, only having my complete logo (Rm Tomás Ferrier, Laboratorio de procesamiento Histologico)
The overleaf, could repeat the same logo, like water logo.
In this face, I need to say: My full data:

Técnico en Anatomía Patológica
Tomás Ferrier Bustos M.P 48207
Av. Ramón Quiroga 817 - 2do piso - Instituto Brandeck.
Córdoba, Argentina
(0351) 156284930
ferrier.tomas@correoluz.com

with respect the colors of card, use your imagination, the original logo color is violet, I haven't chosen a color base for the card.

attached pictures are examples of cards I like your DESIGN.
Attached too, the original logo to my company.

the size of card are:
horizontal: 9cm
vertical: 5,5cm

any question that you have, not doubt to question me,
Hand to work!

Industry/Entity Type

Laboratory

Requirements
Must have
• designers sophisticated, not simples, like show the images attached

```html
<!DOCTYPE html>
<html lang="es">
<head>
<meta charset="utf-8">
<title>RM Tomás Ferrier — Tarjeta personal</title>
<link href="https://fonts.googleapis.com/css2?family=Arimo:wght@400;700&family=Open+Sans:wght@400;600&display=swap" rel="stylesheet">
<style>
  :root {
    --violet: #5b1e78;
    --violet-deep: #3e1056;
    --violet-soft: #9a7cc0;
    --grey: #6f6f72;
    --grey-soft: #b9b9bd;
    --paper: #f7f7f8;
    --paper-shade: #e4e4e7;
    --backdrop: #e8e6eb;
    --white: #ffffff;
  }
  * { box-sizing: border-box; margin: 0; padding: 0; }
  html, body { width: 1200px; height: 1119px; overflow: hidden; }
  body {
    background: var(--backdrop);
    position: relative;
    font-family: "Arimo", Arial, sans-serif;
  }
  .card {
    position: absolute;
    background: linear-gradient(135deg, var(--white), var(--paper) 55%, var(--paper-shade));
    box-shadow: 0 6px 20px rgba(40, 20, 60, 0.18);
    overflow: hidden;
  }

  /* Front face */
  .card-front { left: 50px; top: 130px; width: 640px; height: 391px; }
  .pattern-area {
    position: absolute; left: 0; width: 100%;
    background: linear-gradient(90deg, #ececf0, #e3dcec 50%, #ececf0);
  }
  .pattern-top { top: 0; height: 108px; }
  .pattern-bottom { bottom: 0; height: 108px; }
  .rule { position: absolute; left: 0; width: 100%; }
  .rule-violet { height: 5px; background: var(--violet); }
  .rule-grey { height: 3px; background: var(--grey-soft); }
  .front-rule-1 { top: 96px; }
  .front-rule-2 { top: 106px; }
  .front-rule-3 { top: 284px; }
  .front-rule-4 { top: 293px; }
  .lockup {
    position: absolute; left: 0; right: 0; top: 132px;
    display: flex; flex-direction: column; align-items: center;
  }
  .brand {
    display: flex; align-items: center; gap: 12px;
    font-family: "Open Sans", sans-serif; font-weight: 400;
    color: var(--violet); font-size: 30px; letter-spacing: 4px;
  }
  .brand-mark { width: 22px; height: 22px; background: var(--violet-soft); }
  .tagline {
    margin-top: 10px; padding-top: 6px;
    border-top: 2px solid var(--grey);
    font-family: "Open Sans", sans-serif; font-weight: 600;
    color: var(--grey); font-size: 21px; letter-spacing: 0.3px;
  }

  /* Back face */
  .card-back { left: 760px; top: 60px; width: 400px; height: 655px; }
  .back-shapes { position: absolute; inset: 0; }
  .back-lockup {
    position: absolute; top: 58px; left: 0; right: 0;
    display: flex; flex-direction: column; align-items: center;
  }
  .back-lockup .brand { font-size: 20px; letter-spacing: 2px; gap: 9px; }
  .back-lockup .brand-mark { width: 15px; height: 15px; }
  .back-lockup .tagline { font-size: 13.5px; margin-top: 7px; padding-top: 4px; }
  .holder { position: absolute; top: 178px; left: 0; right: 0; text-align: center; }
  .holder-name { color: var(--violet); font-size: 25px; }
  .holder-title { color: var(--grey); font-size: 18px; margin-top: 14px; }
  .holder-reg { color: var(--grey); font-size: 15px; margin-top: 4px; }
  .watermark {
    position: absolute; top: 340px; right: 36px;
    display: flex; align-items: center; gap: 8px;
    font-family: "Open Sans", sans-serif; font-size: 20px;
    color: #d8d2df; letter-spacing: 2px;
  }
  .watermark-mark { width: 46px; height: 46px; border: 3px solid #ddd6e5; border-radius: 50%; }
  .contact {
    position: absolute; left: 26px; bottom: 22px;
    list-style: none; color: var(--white); font-size: 14px; line-height: 1.45;
  }
  .contact li { display: flex; align-items: flex-start; gap: 7px; }
  .contact svg { flex: none; width: 12px; height: 12px; margin-top: 3px; fill: var(--white); }
  .contact .indent { padding-left: 19px; }
</style>
</head>
<body>

<section class="card card-front" aria-label="Frente de la tarjeta">
  <div class="pattern-area pattern-top" role="img" aria-label="Patrón de hexágonos enlazados en violeta y gris"></div>
  <div class="pattern-area pattern-bottom" role="img" aria-label="Patrón de hexágonos enlazados en violeta y gris"></div>
  <div class="rule rule-violet front-rule-1"></div>
  <div class="rule rule-grey front-rule-2"></div>
  <div class="rule rule-grey front-rule-3"></div>
  <div class="rule rule-violet front-rule-4"></div>
  <div class="lockup">
    <div class="brand"><span class="brand-mark"></span>RM Tomás Ferrier</div>
    <div class="tagline">LABORATORIO DE PROCESAMIENTO HISTOLOGICO</div>
  </div>
</section>

<section class="card card-back" aria-label="Dorso de la tarjeta">
  <svg class="back-shapes" viewBox="0 0 400 655" preserveAspectRatio="none">
    <path d="M0,280 C30,470 150,520 400,520 L400,655 L0,655 Z" fill="var(--violet)"/>
    <path d="M0,280 C25,420 80,480 150,512 L0,655 Z" fill="var(--violet-deep)" opacity="0.35"/>
    <path d="M130,420 C195,485 290,500 400,498 L400,514 C260,516 180,490 130,420 Z" fill="var(--grey-soft)"/>
  </svg>

  <div class="back-lockup">
    <div class="brand"><span class="brand-mark"></span>RM Tomás Ferrier</div>
    <div class="tagline">LABORATORIO DE PROCESAMIENTO HISTOLOGICO</div>
  </div>

  <div class="holder">
    <p class="holder-name">Tomás Ferrier Bustos</p>
    <p class="holder-title">Técnico en Anatomía Patológica</p>
    <p class="holder-reg">M.P 48207</p>
  </div>

  <div class="watermark" aria-hidden="true"><span class="watermark-mark"></span>RM Tomás Ferrier</div>

  <ul class="contact">
    <li><svg viewBox="0 0 12 12"><path d="M2.5 0.5 L4.5 0.5 L5.5 3.5 L4 4.6 C4.7 6 6 7.3 7.4 8 L8.5 6.5 L11.5 7.5 L11.5 9.5 C11.5 10.6 10.6 11.5 9.5 11.5 C4.5 11.2 0.8 7.5 0.5 2.5 C0.5 1.4 1.4 0.5 2.5 0.5 Z"/></svg>(0351) 156284930</li>
    <li><svg viewBox="0 0 12 12"><path d="M0 2 L12 2 L12 10 L0 10 Z M0.8 2.6 L6 6.6 L11.2 2.6" stroke="var(--violet)" stroke-width="0.9"/></svg>ferrier.tomas@correoluz.com</li>
    <li><svg viewBox="0 0 12 12"><path d="M6 0.5 C3.6 0.5 2 2.3 2 4.5 C2 7.5 6 11.5 6 11.5 C6 11.5 10 7.5 10 4.5 C10 2.3 8.4 0.5 6 0.5 Z M6 3 A1.5 1.5 0 1 0 6 6 A1.5 1.5 0 1 0 6 3 Z" fill-rule="evenodd"/></svg>Av. Ramón Quiroga 817 - 2do piso -</li>
    <li class="indent">Instituto Brandeck.</li>
    <li class="indent">Córdoba, Argentina</li>
  </ul>
</section>

</body>
</html>
```